Plotvane Caribbean

We need a vibrant, user friendly and exciting website for our land search company called "plotVane" This application will help individuals locate and or list lots for sale within the Caribbean. We will offer a small cash back incentive to buyers that purchase land from our site, and we will charge a 1%-2% success fee to our sellers once a successful transaction is made. We would like to become a match making site, matching buyers and sellers on our platform. We will also include a service directory and marketing advertisement spot for other service providers for a fee. We would like to see a webdesign incorporating Caribbean colors (blue, green and yellow) with very modern clean lines, very picturesque and easy to use.

Industry/Entity Type

Real Estate

Coding

Number of Pages Required

5+ page

Font styles to use
Sans Serif

Colors
ffffff
85acd3
b768aa
dbdbdb

Requirements
Nice to have
• Scenic photos of the ocean and beautiful landscape

```html
<!DOCTYPE html>
<html lang="en">
<head>
<meta charset="utf-8">
<title>plotVane — Caribbean Land Matchmaking</title>
<link rel="stylesheet" href="https://fonts.googleapis.com/css2?family=Oswald:wght@400;500&family=Open+Sans:wght@400;600;700&display=swap">
<style>
:root{
  --white:#ffffff;
  --sky:#85acd3;
  --orchid:#b768aa;
  --mist:#dbdbdb;
  --lavender:#e6e9f8;
  --ink:#222;
  --text:#555;
  --night:#262b33;
  --card-gray:#c9c9c9;
}
*{margin:0;padding:0;box-sizing:border-box}
html,body{width:1200px;height:3607px;overflow:hidden}
body{position:relative;background:var(--lavender);font-family:"Open Sans",sans-serif;color:var(--text)}
.abs{position:absolute}
.heading{font-family:"Oswald",sans-serif;font-weight:500;color:var(--ink);letter-spacing:1px;text-transform:uppercase}

/* hero */
.hero{left:0;top:0;width:1200px;height:553px;background:linear-gradient(180deg,#6f93b8 0%,#9fc0dc 22%,#3f8fa0 45%,#2aa7b3 62%,#4e8a4a 80%,#d9d2b3 100%)}
.topbar{left:0;top:0;width:1200px;height:101px;background:rgba(20,26,34,.72)}
.brand{left:87px;top:24px;display:flex;align-items:center;gap:12px;font-family:"Oswald",sans-serif;font-weight:500;font-size:34px;color:var(--white);letter-spacing:1px}
.brand-mark{width:40px;height:40px;background:var(--orchid)}
.nav{left:503px;top:29px;display:flex;list-style:none;gap:0}
.nav li{font-family:"Oswald",sans-serif;font-size:15px;color:var(--white);padding:0 20px;height:43px;line-height:43px;letter-spacing:.5px}
.nav li.active{background:var(--orchid)}
.hero-title{left:87px;top:204px;font-family:"Oswald",sans-serif;font-weight:500;font-size:44px;color:var(--white);letter-spacing:1px}
.hero-copy{left:87px;top:262px;width:520px;font-size:15px;line-height:20px;font-style:italic;color:var(--white)}
.btn-sky{background:var(--sky);color:var(--white);font-family:"Oswald",sans-serif;font-size:15px;text-align:center}
.hero-btn{left:87px;top:337px;width:104px;height:36px;line-height:36px}
.arrow{top:340px}

/* search */
.search{left:87px;top:440px;width:1026px;height:233px;background:var(--mist)}
.search-title{left:0;top:22px;width:100%;text-align:center;font-size:26px}
.search-sub{left:0;top:55px;width:100%;text-align:center;font-family:"Oswald",sans-serif;font-size:18px;color:#444}
.select{top:101px;height:48px;background:var(--white);font-size:15px;color:#666;padding:0 26px;display:flex;align-items:center;justify-content:space-between}
.range-label{top:172px;font-size:15px;color:#444}
.range{top:184px;height:4px;background:var(--white)}
.knob{top:172px;width:26px;height:26px;border-radius:50%;background:var(--white);border:3px solid var(--sky)}
.search-btn{left:767px;top:162px;width:235px;height:50px;background:var(--orchid);color:var(--white);font-size:16px;display:flex;align-items:center;justify-content:center;gap:18px}

/* properties */
.section-title{width:1200px;left:0;text-align:center;font-size:28px}
.rule{left:560px;width:80px;height:3px;background:var(--sky)}
.card{width:330px;height:372px;background:var(--white)}
.card-title{left:17px;top:24px;font-size:17px;letter-spacing:.5px;white-space:nowrap}
.card-photo{left:0;top:77px;width:330px;height:216px}
.tag{right:0;top:77px;background:#111;color:var(--white);font-family:"Oswald",sans-serif;font-size:15px;padding:0 14px;height:40px;line-height:40px}
.details{left:104px;top:315px;width:122px;height:34px;line-height:34px;background:#1b1b1b;color:var(--white);font-size:12px;font-weight:700;text-align:center}

/* about */
.about{left:0;top:1660px;width:1200px;height:512px;background:var(--white)}
.about-title{left:87px;top:60px;font-size:28px}
.about-rule{left:87px;top:109px;width:80px;height:3px;background:var(--sky)}
.about-copy{left:87px;top:130px;width:672px;font-size:13px;line-height:19px}
.about-copy p{margin-bottom:16px}
.about-btn{left:87px;top:414px;width:120px;height:44px;line-height:44px}
.about-photo{left:775px;top:55px;width:271px;height:457px;background:linear-gradient(180deg,#f3f3f3 0%,#e4e1e0 40%,#2d3447 70%,#1f2436 100%);border:1px solid #eee}

/* team */
.quote{background:var(--card-gray);color:#eee;font-size:13px;line-height:19px;padding:34px 18px 0}
.quote.featured{background:var(--orchid);color:var(--white);font-size:15px;line-height:22px;padding:40px 18px 0}
.q-icon{width:34px;height:34px;border-radius:50%;background:var(--white);display:flex;align-items:center;justify-content:center}
.avatar{border-radius:50%;background:linear-gradient(180deg,#c9b3a4,#8e6f5e)}
.person{font-size:11px;color:#777;text-align:center;width:240px}

/* services */
.services{left:0;top:2797px;width:1200px;height:426px;background:var(--sky)}
.svc-label{top:157px;width:194px;text-align:center;font-family:"Oswald",sans-serif;font-size:18px;color:#2d3e55}
.svc-box{top:185px;width:194px;height:128px;background:var(--white);display:flex;align-items:center;justify-content:center}
.svc-box.raised{top:180px;box-shadow:0 3px 10px rgba(0,0,0,.25)}
.svc-shape{width:110px;height:56px;background:#cfd4da}
.dot{top:354px;width:12px;height:12px;border-radius:50%;background:var(--white)}

/* signup */
.signup{left:0;top:3223px;width:1200px;height:115px;background:var(--orchid)}
.signup-title{left:87px;top:30px;font-family:"Oswald",sans-serif;font-size:34px;color:var(--white);letter-spacing:1px}
.signup-sub{left:87px;top:74px;font-size:11px;color:#f3e3f0}
.email{left:565px;top:36px;width:366px;height:41px;background:var(--white);font-size:13px;color:#555;padding:12px 22px}
.submit{left:943px;top:36px;width:127px;height:41px;line-height:41px}

/* footer */
.footer{left:0;top:3338px;width:1200px;height:269px;background:var(--night);color:#ddd}
.foot-brand{left:87px;top:82px;display:flex;align-items:center;gap:14px;font-family:"Oswald",sans-serif;font-weight:500;font-size:48px;color:var(--white);letter-spacing:1px}
.foot-mark{width:52px;height:52px;background:var(--white)}
.reach{left:541px;top:38px;font-family:"Oswald",sans-serif;font-size:22px;color:var(--white);letter-spacing:1px}
.reach-rule{left:541px;top:79px;width:572px;height:1px;background:#4a505a}
.contact{left:541px;top:101px;width:572px;display:flex;gap:14px;font-size:12px;color:#ddd;align-items:center;white-space:nowrap}
.contact span{display:flex;align-items:center;gap:7px}
.contact .mail{margin-left:auto}
.socials{left:541px;top:153px;display:flex;gap:16px}
.socials i{width:14px;height:14px;border-radius:50%;background:#ddd;display:block}
.foot-line{left:0;top:202px;width:1200px;height:1px;background:#3d434c}
.foot-nav{left:87px;top:233px;font-size:12px;color:#ccc;word-spacing:4px}
.copyright{right:87px;top:233px;font-size:12px;color:#ccc}
</style>
</head>
<body>

<!-- hero -->
<div class="abs hero" role="img" aria-label="Scenic Caribbean bay with turquoise water, green hills and a sandy beach"></div>
<div class="abs topbar"></div>
<div class="abs brand"><span class="brand-mark"></span>PLOTVANE</div>
<ul class="abs nav">
  <li class="active">HOME</li><li>BUY</li><li>SELL</li><li>SERVICES</li><li>DEALS</li><li>AGENTS</li><li>CONTACT US</li>
</ul>
<h1 class="abs hero-title">WELCOME TO PLOTVANE</h1>
<p class="abs hero-copy">We will offer a small cash back incentive to buyers that purchase land from our site, and we will charge a 1%-2% success fee to our sellers once a successful transaction is made.</p>
<div class="abs btn-sky hero-btn">READ MORE</div>
<svg class="abs arrow" style="left:6px" width="16" height="28" viewBox="0 0 16 28"><path d="M13 3 3 14l10 11" fill="none" stroke="#fff" stroke-width="3"/></svg>
<svg class="abs arrow" style="left:1178px" width="16" height="28" viewBox="0 0 16 28"><path d="M3 3l10 11L3 25" fill="none" stroke="#fff" stroke-width="3"/></svg>

<!-- search -->
<section class="abs search">
  <div class="abs heading search-title">LAND LOVERS</div>
  <div class="abs search-sub">Matching Buyers and Sellers</div>
  <div class="abs select" style="left:24px;width:310px">List of Caribbean
    <svg width="12" height="16" viewBox="0 0 12 16"><path d="M6 1a5 5 0 0 0-5 5c0 4 5 9 5 9s5-5 5-9a5 5 0 0 0-5-5zm0 7a2 2 0 1 1 0-4 2 2 0 0 1 0 4z" fill="#666"/></svg></div>
  <div class="abs select" style="left:353px;width:315px">Cash Buyer
    <svg width="12" height="8" viewBox="0 0 12 8"><path d="M1 1l5 5 5-5" fill="none" stroke="#666" stroke-width="1.6"/></svg></div>
  <div class="abs select" style="left:683px;width:317px">Mountain
    <svg width="12" height="8" viewBox="0 0 12 8"><path d="M1 1l5 5 5-5" fill="none" stroke="#666" stroke-width="1.6"/></svg></div>
  <div class="abs range-label" style="left:36px">Price</div>
  <div class="abs range" style="left:104px;width:262px"></div>
  <div class="abs knob" style="left:128px"></div>
  <div class="abs range-label" style="left:392px">Size</div>
  <div class="abs range" style="left:440px;width:244px"></div>
  <div class="abs knob" style="left:494px"></div>
  <div class="abs search-btn">Search
    <svg width="16" height="16" viewBox="0 0 16 16"><circle cx="6.5" cy="6.5" r="5" fill="none" stroke="#fff" stroke-width="2"/><path d="M10 10l5 5" stroke="#fff" stroke-width="2.4"/></svg></div>
</section>

<!-- latest properties -->
<h2 class="abs heading section-title" style="top:740px">LATEST PROPERTIES</h2>
<div class="abs rule" style="top:786px"></div>

<article class="abs card" style="left:87px;top:830px">
  <h3 class="abs heading card-title">BRITISH VIRGIN ISLANDS BVI</h3>
  <div class="abs card-photo" role="img" aria-label="Beachfront villa with palms beside a blue bay" style="background:linear-gradient(180deg,#b6d3ea,#3f8fb0 50%,#5f8a52 75%,#d9dad2)"></div>
  <div class="abs tag">FOR SALE</div><div class="abs details">MORE DETAILS</div>
</article>
<article class="abs card" style="left:435px;top:830px">
  <h3 class="abs heading card-title">UNITED STATES VIRGIN ISLANDS USVI</h3>
  <div class="abs card-photo" role="img" aria-label="Hillside estate house framed by a large tree" style="background:linear-gradient(180deg,#d9e4ee,#9fb38c 45%,#5c6b3c 80%,#8a7a5c)"></div>
  <div class="abs tag">FOR SALE</div><div class="abs details">MORE DETAILS</div>
</article>
<article class="abs card" style="left:782px;top:830px">
  <h3 class="abs heading card-title">ANTIGUA &amp; BARBUDA</h3>
  <div class="abs card-photo" role="img" aria-label="Green hills dotted with white homes" style="background:linear-gradient(180deg,#c7d6de,#5f8a45 35%,#4a7035 70%,#7e8c66)"></div>
  <div class="abs tag">FOR SALE</div><div class="abs details">MORE DETAILS</div>
</article>
<article class="abs card" style="left:87px;top:1219px">
  <h3 class="abs heading card-title">ST. KITTS &amp; NEVIS</h3>
  <div class="abs card-photo" role="img" aria-label="Jungle shoreline with a small house on stilts over water" style="background:linear-gradient(180deg,#2f5a35,#3f7a3e 45%,#2f8f8a 75%,#1f7a7a)"></div>
  <div class="abs tag">FOR SALE</div><div class="abs details">MORE DETAILS</div>
</article>
<article class="abs card" style="left:435px;top:1219px">
  <h3 class="abs heading card-title">JAMAICA</h3>
  <div class="abs card-photo" role="img" aria-label="Sandy beach with mountains across the sea" style="background:linear-gradient(180deg,#2f78c4,#8fbde6 40%,#4a8fae 62%,#d8c9a0 85%)"></div>
  <div class="abs tag">FOR SALE</div><div class="abs details">MORE DETAILS</div>
</article>
<article class="abs card" style="left:782px;top:1219px">
  <h3 class="abs heading card-title">ST. MARTIN</h3>
  <div class="abs card-photo" role="img" aria-label="Forested coast with a wooden hut above turquoise water" style="background:linear-gradient(180deg,#6fa0d0,#3f7a3a 35%,#356b30 65%,#2fa3a0)"></div>
  <div class="abs tag">FOR SALE</div><div class="abs details">MORE DETAILS</div>
</article>

<!-- about -->
<section class="abs about">
  <h2 class="abs heading about-title">ABOUT PLOTVANE</h2>
  <div class="abs about-rule"></div>
  <div class="abs about-copy">
    <p>plotVane is a Caribbean matchmaking site similar to online dating sites. The difference is, plotVane is all about creating a platform that connects the right buyers with the right sellers. We intend to find the perfect slice of paradise for our buyers and the highest exchange for our sellers.</p>
    <p>We believe that every customer who is looking for land (single house lot, or large track of land for major development) within the Caribbean can find it right here. Maybe you are desirous of selling or leasing your land and need a quick sale, sign up to our fast track system and find cash buyers today.</p>
    <p>For those that are interested in making additional income, please join our team of Virtual Agents and earn extra cash from anywhere in the world; this is an opportunity of a lifetime! If you do not find what you are looking for, sign up to our buyers list and be the first to receive direct land deals that match your criteria.</p>
  </div>
  <div class="abs btn-sky about-btn">Read More</div>
  <div class="abs about-photo" role="img" aria-label="Portrait of a smiling agent in a navy blazer"></div>
</section>

<!-- join our team -->
<h2 class="abs heading section-title" style="top:2246px">JOIN OUR TEAM</h2>
<div class="abs rule" style="top:2294px"></div>

<div class="abs quote" style="left:87px;top:2393px;width:194px;height:108px">Listed my hillside lot and found a serious buyer within weeks.</div>
<div class="abs q-icon" style="left:98px;top:2376px"><svg width="16" height="12" viewBox="0 0 16 12"><path d="M0 12V6l3-6h3L4 5h2v7zm9 0V6l3-6h3l-2 5h2v7z" fill="#bbb"/></svg></div>
<div class="abs quote featured" style="left:327px;top:2369px;width:306px;height:164px">"Sign up right now and receive great deals directly into your inbox and cash back on your first purchase!"</div>
<div class="abs q-icon" style="left:350px;top:2349px;width:40px;height:40px;background:var(--orchid);border:3px solid var(--white)"><svg width="16" height="12" viewBox="0 0 16 12"><path d="M0 12V6l3-6h3L4 5h2v7zm9 0V6l3-6h3l-2 5h2v7z" fill="#fff"/></svg></div>
<svg class="abs" style="left:470px;top:2532px" width="24" height="12" viewBox="0 0 24 12"><path d="M0 0h24L12 12z" fill="#b768aa"/></svg>
<div class="abs quote" style="left:661px;top:2393px;width:197px;height:108px">Clear listings, quick replies and a fair fee for sellers.</div>
<div class="abs q-icon" style="left:672px;top:2376px"><svg width="16" height="12" viewBox="0 0 16 12"><path d="M0 12V6l3-6h3L4 5h2v7zm9 0V6l3-6h3l-2 5h2v7z" fill="#bbb"/></svg></div>
<div class="abs quote" style="left:902px;top:2393px;width:211px;height:108px">Great way to compare island plots before booking a flight.</div>
<div class="abs q-icon" style="left:913px;top:2376px"><svg width="16" height="12" viewBox="0 0 16 12"><path d="M0 12V6l3-6h3L4 5h2v7zm9 0V6l3-6h3l-2 5h2v7z" fill="#bbb"/></svg></div>

<div class="abs avatar" style="left:161px;top:2520px;width:64px;height:64px" role="img" aria-label="Team member portrait"></div>
<div class="abs person" style="left:73px;top:2594px">Anya R. Castries, LC</div>
<div class="abs avatar" style="left:436px;top:2555px;width:96px;height:96px;border:3px solid #111" role="img" aria-label="Featured team member portrait"></div>
<div class="abs person" style="left:364px;top:2670px;font-size:17px;color:var(--orchid)">Marisol T. Harbour</div>
<div class="abs avatar" style="left:737px;top:2520px;width:64px;height:64px" role="img" aria-label="Team member portrait"></div>
<div class="abs person" style="left:649px;top:2594px">Anya R. Castries, LC</div>
<div class="abs avatar" style="left:975px;top:2520px;width:64px;height:64px" role="img" aria-label="Team member portrait"></div>
<div class="abs person" style="left:887px;top:2594px">Anya R. Castries, LC</div>

<!-- service links -->
<section class="abs services">
  <h2 class="abs heading section-title" style="top:52px">SERVICE LINKS</h2>
  <div class="abs rule" style="top:100px;background:var(--white)"></div>
  <div class="abs svc-label" style="left:87px">Developers</div>
  <div class="abs svc-label" style="left:296px">Surveyors</div>
  <div class="abs svc-label" style="left:505px">Appraisers</div>
  <div class="abs svc-label" style="left:714px">Landscapers</div>
  <div class="abs svc-label" style="left:922px">Financiers</div>
  <div class="abs svc-box" style="left:87px"><div class="svc-shape"></div></div>
  <div class="abs svc-box" style="left:296px"><div class="svc-shape"></div></div>
  <div class="abs svc-box raised" style="left:505px"><div class="svc-shape"></div></div>
  <div class="abs svc-box" style="left:714px"><div class="svc-shape"></div></div>
  <div class="abs svc-box" style="left:922px"><div class="svc-shape"></div></div>
  <div class="abs dot" style="left:572px"></div>
  <div class="abs dot" style="left:594px;background:var(--orchid)"></div>
  <div class="abs dot" style="left:616px"></div>
</section>

<!-- sign up -->
<section class="abs signup">
  <div class="abs signup-title">SIGN UP TODAY</div>
  <div class="abs signup-sub">Sign up to receive timely, useful information in your inbox.</div>
  <div class="abs email">EMAIL</div>
  <div class="abs btn-sky submit">SUBMIT</div>
</section>

<!-- footer -->
<footer class="abs footer">
  <div class="abs foot-brand"><span class="foot-mark"></span>PLOTVANE</div>
  <div class="abs reach">TO REACH US:</div>
  <div class="abs reach-rule"></div>
  <div class="abs contact">
    <span><svg width="11" height="15" viewBox="0 0 12 16"><path d="M6 1a5 5 0 0 0-5 5c0 4 5 9 5 9s5-5 5-9a5 5 0 0 0-5-5zm0 7a2 2 0 1 1 0-4 2 2 0 0 1 0 4z" fill="#ddd"/></svg>415 Coral Ridge Road, Bridgetown, Caribbean.</span>
    <span><svg width="13" height="13" viewBox="0 0 16 16"><path d="M3 1l3 3-2 2c1 2 3 4 6 6l2-2 3 3-2 2C7 15 1 9 1 3z" fill="#ddd"/></svg>555-014-220</span>
    <span class="mail"><svg width="15" height="11" viewBox="0 0 16 12"><rect width="16" height="12" fill="#ddd"/><path d="M0 0l8 6 8-6" fill="none" stroke="#262b33" stroke-width="1.4"/></svg>hello@plotvane.example</span>
  </div>
  <div class="abs socials"><i></i><i></i><i></i><i></i><i></i></div>
  <div class="abs foot-line"></div>
  <div class="abs foot-nav">Home | Buy | Sell | Services | Deals | Agents | Contact Us</div>
  <div class="abs copyright">Copyright © 2017 plotVane.</div>
</footer>

</body>
</html>
```